skyMARLOW Helicopter Tour WordPress Website Design

SkyMARLOW (skymarlow-tours.example) is a premium helicopter tour company offering scenic flights in two Florida cities: Tampa and Sarasota. We are seeking a full Wordpress website redesign that is modern, upbeat, inviting, and highly conversion‑focused. The new site should feel energetic and trustworthy, reflect the excitement of helicopter sightseeing, and maintain our recognizable SkyMARLOW color palette—while updating the overall look to feel fresh, clean, and current.
The website must be SEO‑friendly, mobile‑optimized, and easy to navigate. It should highlight our 5‑star customer reviews, showcase our tours clearly, and integrate seamlessly with TicketPine for instant online booking. The design should support a premium aviation experience while remaining friendly and accessible to tourists, families, couples, and adventure seekers.

These elements are essential and must be included in the design:

Brand & UX:
- Modern, upbeat, inviting design
- SEO‑friendly structure and layout
- Easy navigation and clear user flow
- Light grey “SM” background logo watermark (as used on current site)
- Clean, aviation‑inspired typography and layout

Conversion Features:
- Instant booking above the fold (TicketPine integration)
- Live Google Reviews carousel
- Tour comparison table (duration, route, price, etc.)
- FAQ expandable section
- Gift Cards page (highlighted as a major offering)
- What to Expect timeline (Arrive → Check‑In → Safety Briefing → Flight → Photos)
- Weather transparency widget (clear messaging about weather‑dependent flights

Content Structure:
- Separate pages for Tampa, Sarasota, and Gender Reveal Flights
- Pilot/Team profiles with short bios
- Highlighted features:
- Doors‑Off option
- Sunset flights
- Romantic packages
- Champagne add‑ons

Colors:
Use the existing SkyMARLOW palette as the foundation, but modernize it.
- Background: Clean with the light grey “SM” watermark integrated tastefully.
The overall color direction should feel bright, premium, energetic, and trustworthy

Target Market(s)

Tourists visiting Tampa or Sarasota, Families looking for memorable activities, Couples seeking romantic experiences (sunset flights, proposals, anniversaries), Adventure seekers and content creators, Locals celebrating birthdays, holidays, or special occasions, Gender reveal clients looking for a unique aerial reveal experience

Industry/Entity Type

Travel & Tourism / Aviation / Helicopter Tours / Experience‑based Activities

Requirements
Must have
• These elements are essential and must be included in the design: Brand & UX - Modern, upbeat, inviting design / SEO‑friendly structure and layout / Easy navigation and clear user flow / Light grey “SM” background logo watermark (as used on current site) / Clean, aviation‑inspired typography and layout
Nice to have
• Interactive route map showing flight paths / Subtle motion or parallax effects in hero sections / Animated icons or micro‑interactions / Social media integration (Instagram grid, TikTok clips) / Sticky mobile booking bar / Video header or short aerial footage loop / Subtle aviation‑themed graphic elements (rotor blur, sky gradients, etc.
Should not have
• No dark, heavy, or overly moody themes / No outdated fonts or overly playful typography / No cluttered layouts or excessive text blocks / No stocky, generic tourism imagery / No slow‑loading animations or heavy effects that hurt SEO

```html
<!DOCTYPE html>
<html lang="en">
<head>
<meta charset="utf-8">
<title>SkyMARLOW — FAQ &amp; Footer</title>
<link href="https://fonts.googleapis.com/css2?family=Poppins:wght@600;700&family=Roboto:wght@400;500;700&display=swap" rel="stylesheet">
<style>
:root{
  --sky-top:#cadffc;
  --sky-bottom:#a5c8fb;
  --card:#ffffff;
  --ink:#2a2d33;
  --muted:#6b7280;
  --brand:#0a7bff;
  --brand-logo:#2d7fd0;
  --footer:#212429;
  --footer-text:#d4d7dc;
  --footer-muted:#a3a8b0;
  --rule:#363a41;
}
*{box-sizing:border-box;margin:0;padding:0}
html,body{width:927px;height:1200px;overflow:hidden;background:#fff;font-family:'Roboto',sans-serif}
.page{position:relative;width:927px;height:1200px}
.faq{position:absolute;left:0;top:0;width:927px;height:533px;background:linear-gradient(180deg,var(--sky-top),var(--sky-bottom));overflow:hidden}
.faq__lead{position:absolute;top:-9px;width:100%;text-align:center;font-size:12px;color:var(--muted)}
.faq__item{position:absolute;left:181px;width:565px;height:46px;background:var(--card);border-radius:6px;box-shadow:0 3px 10px rgba(40,80,150,.12);display:flex;align-items:center;justify-content:space-between;padding:0 18px 0 17px}
.faq__q{font-family:'Poppins',sans-serif;font-weight:700;font-size:12px;color:var(--ink)}
.faq__chev{width:11px;height:11px}
.faq__more{position:absolute;top:407px;width:100%;text-align:center;font-size:10.5px;color:var(--muted)}
.btn{display:flex;align-items:center;justify-content:center;gap:6px;background:var(--brand);color:#fff;font-weight:700;border-radius:4px;text-decoration:none}
.faq__contact{position:absolute;left:403px;top:439px;width:121px;height:40px;font-size:12px;box-shadow:0 6px 14px rgba(10,90,200,.25)}
.footer{position:absolute;left:0;top:533px;width:927px;height:341px;background:var(--footer);color:var(--footer-text)}
.brand{position:absolute;left:51px;top:50px;display:flex;align-items:center;gap:8px}
.brand__dot{width:14px;height:14px;border-radius:50%;background:var(--brand-logo)}
.brand__name{font-family:'Poppins',sans-serif;font-weight:700;font-size:19px;color:var(--brand-logo)}
.footer__about{position:absolute;left:51px;top:133px;width:185px;font-size:10.5px;line-height:16.2px;color:var(--footer-text)}
.social{position:absolute;left:51px;top:210px;display:flex;gap:10px}
.social__item{width:16px;height:16px;border-radius:50%;background:var(--footer-text)}
.col{position:absolute;top:44px}
.col__title{font-family:'Poppins',sans-serif;font-weight:700;font-size:13.5px;color:#fff;margin-bottom:9px}
.col__list{list-style:none}
.col__list li{font-size:10.5px;line-height:21.7px}
.contact li{display:flex;align-items:flex-start;gap:8px;font-size:10.5px;line-height:16px;margin-bottom:8px}
.contact svg{width:10px;height:10px;margin-top:3px;flex:none}
.footer__book{position:absolute;left:686px;top:172px;width:82px;height:32px;font-size:10.5px}
.footer__rule{position:absolute;left:51px;top:261px;width:825px;height:1px;background:var(--rule)}
.footer__copy{position:absolute;left:51px;top:283px;font-size:9.5px;color:var(--footer-muted)}
.legal{position:absolute;right:51px;top:283px;display:flex;gap:16px;font-size:9.5px;color:var(--footer-muted)}
</style>
</head>
<body>
<div class="page">
  <section class="faq">
    <p class="faq__lead">Get answers to common questions about our helicopter tours</p>
    <div class="faq__item" style="top:42px"><span class="faq__q">How long are the helicopter tours?</span><svg class="faq__chev" viewBox="0 0 12 12"><path d="M2 4l4 4 4-4" fill="none" stroke="#0a7bff" stroke-width="1.5"/></svg></div>
    <div class="faq__item" style="top:99px"><span class="faq__q">What happens if the weather is bad?</span><svg class="faq__chev" viewBox="0 0 12 12"><path d="M2 4l4 4 4-4" fill="none" stroke="#0a7bff" stroke-width="1.5"/></svg></div>
    <div class="faq__item" style="top:156px"><span class="faq__q">How many people can fly in one helicopter?</span><svg class="faq__chev" viewBox="0 0 12 12"><path d="M2 4l4 4 4-4" fill="none" stroke="#0a7bff" stroke-width="1.5"/></svg></div>
    <div class="faq__item" style="top:213px"><span class="faq__q">Can I take photos during the flight?</span><svg class="faq__chev" viewBox="0 0 12 12"><path d="M2 4l4 4 4-4" fill="none" stroke="#0a7bff" stroke-width="1.5"/></svg></div>
    <div class="faq__item" style="top:270px"><span class="faq__q">What should I wear for my helicopter tour?</span><svg class="faq__chev" viewBox="0 0 12 12"><path d="M2 4l4 4 4-4" fill="none" stroke="#0a7bff" stroke-width="1.5"/></svg></div>
    <div class="faq__item" style="top:327px"><span class="faq__q">Are gift cards available?</span><svg class="faq__chev" viewBox="0 0 12 12"><path d="M2 4l4 4 4-4" fill="none" stroke="#0a7bff" stroke-width="1.5"/></svg></div>
    <p class="faq__more">Still have questions?</p>
    <a class="btn faq__contact" href="#contact"><svg width="13" height="10" viewBox="0 0 13 10"><rect width="13" height="10" rx="1.5" fill="#fff"/><path d="M1 1.5l5.5 4 5.5-4" fill="none" stroke="#0a7bff" stroke-width="1.3"/></svg>Contact Us</a>
  </section>

  <footer class="footer">
    <div class="brand"><span class="brand__dot"></span><span class="brand__name">SkyMARLOW</span></div>
    <p class="footer__about">Premium helicopter tours offering unforgettable aerial experiences over Tampa Bay and Sarasota's stunning coastline.</p>
    <div class="social" aria-label="Social links"><span class="social__item"></span><span class="social__item"></span><span class="social__item"></span><span class="social__item"></span></div>

    <div class="col" style="left:263px">
      <h3 class="col__title">Our Tours</h3>
      <ul class="col__list"><li>Tampa Helicopter Tours</li><li>Sarasota Helicopter Tours</li><li>Gender Reveal Flights</li><li>Gift Cards</li></ul>
    </div>
    <div class="col" style="left:475px">
      <h3 class="col__title">Company</h3>
      <ul class="col__list"><li>About Us</li><li>What to Expect</li><li>Reviews</li><li>FAQs</li><li>Contact Us</li></ul>
    </div>
    <div class="col" style="left:686px">
      <h3 class="col__title">Get in Touch</h3>
      <ul class="col__list contact">
        <li><svg viewBox="0 0 10 12"><path d="M5 0a4 4 0 0 0-4 4c0 3 4 8 4 8s4-5 4-8a4 4 0 0 0-4-4z" fill="#0a7bff"/><circle cx="5" cy="4" r="1.4" fill="#212429"/></svg>Tampa &amp; Sarasota<br>Florida</li>
        <li><svg viewBox="0 0 12 12"><path d="M2.5 0.5l2 0.5 1 3-1.5 1.2a7 7 0 0 0 3 3L8.2 6.7l3 1 0.5 2L10 11.5C5 11.5 0.5 7 0.5 2z" fill="#0a7bff"/></svg>(555) 014-2290</li>
        <li><svg viewBox="0 0 12 10"><rect width="12" height="10" rx="1" fill="#0a7bff"/><path d="M1 1.5l5 3.5 5-3.5" fill="none" stroke="#212429" stroke-width="1.1"/></svg>info@skymarlow-tours.example</li>
      </ul>
    </div>
    <a class="btn footer__book" href="#book">Book Now</a>

    <div class="footer__rule"></div>
    <p class="footer__copy">© 2026 SkyMARLOW. All rights reserved.</p>
    <nav class="legal"><span>Privacy Policy</span><span>Terms of Service</span><span>Cancellation Policy</span></nav>
  </footer>
</div>
</body>
</html>
```